Fundraising Event Logistics and Strategy

We need a web design for our non-profit fundraising event strategy business. We help non-profits streamline gala and 'pre registered' event operations to maximize their funds raised. We would like a simple design, our company colors are dark blue and silver. The design should be clean and also allow for some partner logos. I have attached some current logo collateral. Company is Dana Whitcombe & Co dba GalaPivotry, but neither logo has to be used.
Target Market(s)
Non Profit Organizations
Industry/Entity Type
Business
Number of Pages Required
3 page
Requirements
Must have
- Contact Us Form
- Partner Logos with Links

```html
<!DOCTYPE html>
<html lang="en">
<head>
<meta charset="utf-8">
<title>GalaPivotry – Event Fundraising</title>
<link href="https://fonts.googleapis.com/css2?family=Open+Sans:wght@300;400;600&family=Raleway:wght@300;400;500;600&display=swap" rel="stylesheet">
<style>
  :root{
    --navy:#0b3a6e;
    --blue:#1167b8;
    --blue-bright:#1e86d6;
    --blue-deep:#0a4c91;
    --field:#0d3566;
    --silver:#c9ccd1;
    --grey-bg:#f2f3f5;
    --footer-bg:#e4e5e7;
    --text:#3b3f45;
    --muted:#7b8089;
    --white:#ffffff;
  }
  *{box-sizing:border-box;margin:0;padding:0}
  html,body{width:745px;height:1200px;overflow:hidden}
  body{background:var(--white);font-family:"Open Sans",Arial,sans-serif;color:var(--text);position:relative}

  .site-header{height:46px;display:flex;align-items:center;justify-content:space-between;padding:0 50px 0 96px;background:var(--white)}
  .brand{display:flex;align-items:center;gap:8px;font-family:"Raleway",Arial,sans-serif;font-weight:500;font-size:12px;color:var(--navy)}
  .brand-mark{width:10px;height:10px;border-radius:50%;background:var(--silver)}
  .main-nav{display:flex;gap:22px}
  .main-nav a{font-size:8px;letter-spacing:.5px;color:var(--muted);text-decoration:none;text-transform:uppercase}
  .main-nav a.active{color:var(--navy);font-weight:600}

  .hero{position:relative;height:324px}
  .hero-photo{position:absolute;inset:0;background:linear-gradient(160deg,#9fb4c8 0%,#6f8aa6 35%,#4a6887 65%,#2f4d6d 100%)}
  .hero-copy{position:absolute;left:0;right:0;top:130px;text-align:center;color:var(--white);font-family:"Raleway",Arial,sans-serif}
  .hero-copy h1{font-size:25px;font-weight:500;letter-spacing:1px}
  .hero-copy p{font-size:15px;font-weight:500;letter-spacing:.6px;margin-top:2px}

  .about{text-align:center;padding:28px 110px 0}
  .section-title{font-family:"Raleway",Arial,sans-serif;font-weight:400;font-size:21px;color:#444;letter-spacing:.5px}
  .about p{font-size:6.6px;line-height:1.55;color:var(--muted);margin-top:8px}

  .services{margin-top:40px;text-align:center}
  .services .section-title{color:var(--blue);font-size:17px}
  .service-band{margin:14px 0 0;background:var(--grey-bg);height:155px;border-top:1px solid #e3e4e7;display:flex;justify-content:center;gap:50px;padding-top:30px}
  .service{width:130px}
  .hex{width:52px;height:58px;margin:0 auto}
  .service h3{font-family:"Raleway",Arial,sans-serif;font-weight:500;font-size:10.5px;color:#333;margin-top:12px}
  .service p{font-size:5.6px;line-height:1.5;color:var(--muted);margin-top:4px}

  .contact{position:absolute;top:740px;left:0;width:745px;height:190px;background:linear-gradient(180deg,var(--blue-bright) 0%,var(--blue) 40%,var(--blue-deep) 100%)}
  .contact-title{height:36px;background:rgba(255,255,255,.12);display:flex;align-items:center;justify-content:center;color:var(--white);font-family:"Raleway",Arial,sans-serif;font-size:13px;margin:14px 170px 0}
  .contact-form{width:405px;margin:12px auto 0}
  .field-row{display:flex;gap:8px}
  .field{flex:1;height:16px;background:var(--field);color:#c3d3e6;font-size:6px;padding:4px 6px}
  .field.message{height:44px;margin-top:6px}
  .actions{display:flex;justify-content:center;gap:8px;margin-top:10px}
  .btn{width:60px;height:15px;font-size:6.5px;color:var(--white);display:flex;align-items:center;justify-content:center;letter-spacing:.5px}
  .btn.submit{background:var(--blue-bright);border:1px solid #5fb2ef}
  .btn.reset{border:1px solid #9cc6ec}

  .partners{position:absolute;top:955px;left:0;width:745px;text-align:center}
  .partners .section-title{font-size:16px}
  .partner-grid{position:relative;height:110px;margin-top:10px}
  .partner{position:absolute;border-radius:3px}

  .site-footer{position:absolute;top:1128px;left:0;width:745px;height:72px;background:var(--footer-bg);padding:14px 96px 0}
  .footer-top{display:flex;justify-content:space-between;align-items:center}
  .footer-nav{display:flex;gap:5px;font-size:7px;color:#555}
  .footer-nav span{color:#999}
  .social{display:flex;gap:4px}
  .social i{display:block;width:11px;height:11px;border-radius:50%;background:var(--blue-bright)}
  .social i.red{background:#d9463b}
  .copyright{font-size:5px;color:#888;margin-top:4px}
</style>
</head>
<body>
  <header class="site-header">
    <div class="brand"><span class="brand-mark"></span>Dana Whitcombe &amp; Co</div>
    <nav class="main-nav">
      <a class="active" href="#">Home</a><a href="#">About Us</a><a href="#">Services</a><a href="#">Partners</a><a href="#">Contact</a>
    </nav>
  </header>

  <section class="hero">
    <div class="hero-photo" role="img" aria-label="Photo of several hands dropping coins into a white piggy bank"></div>
    <div class="hero-copy">
      <h1>EVENT FUNDRAISING</h1>
      <p>FUSCE ULTRICIES ORCI AC FEUGIAT SUSCIPIT</p>
    </div>
  </section>

  <section class="about">
    <h2 class="section-title">ABOUT OUR COMPANY</h2>
    <p>We help non-profit teams plan galas and pre-registered events with clear steps, smart timing and calm logistics so every guest counts and more funds reach the cause.</p>
    <p>From first guest list to final thank-you, our strategists handle registration, auction flow, volunteer roles and reporting. You focus on your mission while we keep the evening organised, on budget and on time.</p>
  </section>

  <section class="services">
    <h2 class="section-title">Services Provides</h2>
    <div class="service-band">
      <div class="service">
        <svg class="hex" viewBox="0 0 52 58"><polygon points="26,0 52,14.5 52,43.5 26,58 0,43.5 0,14.5" fill="var(--blue-deep)"/><path d="M26 38 C14 30 16 20 22 20 C24 20 26 22 26 24 C26 22 28 20 30 20 C36 20 38 30 26 38Z" fill="#fff"/></svg>
        <h3>Non Profit Fundraising</h3>
        <p>Planning and guidance for charities who want each event to raise more with less stress.</p>
      </div>
      <div class="service">
        <svg class="hex" viewBox="0 0 52 58"><polygon points="26,0 52,14.5 52,43.5 26,58 0,43.5 0,14.5" fill="var(--blue-deep)"/><circle cx="25" cy="30" r="11" fill="#fff"/><path d="M27 17 A11 11 0 0 1 38 28 L27 28Z" fill="#fff" stroke="var(--blue-deep)" stroke-width="1.5"/><path d="M25 30 L25 19 M25 30 L34 36" stroke="var(--blue-deep)" stroke-width="1.5"/></svg>
        <h3>Business &amp; Event Strategy</h3>
        <p>Clear goals, sponsor plans and event timelines built around your audience and budget.</p>
      </div>
      <div class="service">
        <svg class="hex" viewBox="0 0 52 58"><polygon points="26,0 52,14.5 52,43.5 26,58 0,43.5 0,14.5" fill="var(--blue-deep)"/><rect x="15" y="20" width="22" height="19" rx="2" fill="#fff"/><rect x="15" y="20" width="22" height="5" fill="#cfe0f2"/><path d="M20 17v6M32 17v6" stroke="#fff" stroke-width="2"/><path d="M20 31l4 4 8-8" stroke="var(--blue-deep)" stroke-width="1.8" fill="none"/></svg>
        <h3>Helping Event Operation</h3>
        <p>On-site teams run check-in, bidding and payments so the night runs smoothly.</p>
      </div>
    </div>
  </section>

  <section class="contact">
    <div class="contact-title">Quick Contact Form</div>
    <form class="contact-form">
      <div class="field-row">
        <div class="field">Your Name</div>
        <div class="field">Email address</div>
        <div class="field">Phone no.</div>
      </div>
      <div class="field message">Message</div>
      <div class="actions">
        <div class="btn submit">SUBMIT</div>
        <div class="btn reset">RESET</div>
      </div>
    </form>
  </section>

  <section class="partners">
    <h2 class="section-title">Our Partners</h2>
    <div class="partner-grid">
      <div class="partner" style="left:155px;top:20px;width:34px;height:34px;border-radius:50%;background:#e0a33a"></div>
      <div class="partner" style="left:220px;top:22px;width:48px;height:28px;background:#e2733a"></div>
      <div class="partner" style="left:292px;top:18px;width:56px;height:30px;background:#3a3a3a"></div>
      <div class="partner" style="left:370px;top:22px;width:56px;height:24px;background:#2f5aa8"></div>
      <div class="partner" style="left:455px;top:16px;width:36px;height:38px;background:#6f7c8f"></div>
      <div class="partner" style="left:220px;top:66px;width:52px;height:28px;background:#b8772f"></div>
      <div class="partner" style="left:300px;top:66px;width:40px;height:34px;border-radius:50%;background:#d66a2c"></div>
      <div class="partner" style="left:372px;top:66px;width:36px;height:32px;background:#b8202c"></div>
      <div class="partner" style="left:428px;top:72px;width:46px;height:18px;background:#d2232a"></div>
    </div>
  </section>

  <footer class="site-footer">
    <div class="footer-top">
      <div class="footer-nav">HOME <span>|</span> ABOUT US <span>|</span> SERVICES <span>|</span> PARTNERS <span>|</span> CONTACT</div>
      <div class="social"><i></i><i></i><i></i><i class="red"></i></div>
    </div>
    <p class="copyright">2024 GalaPivotry. All rights reserved.</p>
  </footer>
</body>
</html>
```